Nutrigenomics Business card design

Nutrigenomics is an exciting emerging field where I sequence the DNA from a saliva swab and then tailor a personalised nutritional program according to the persons genetics. It is possible to turn down undesirable genes that may be stuck "on" all the time causing inflammation etc. Equally important we switch "on" genes that might be stuck "off" as is often the case with autism. A large portion of my clients are autistic children. We see huge changes in functionality with the appropriate changes in diet to regulate their gene expression. This technology is definitely the way of the future.
I need a logo that will clearly show the combination of genetics with nutrition. The word "Nutrigenomics" still isn't in common use yet. I'm thinking maybe a DNA helix - (I think most people associate a helix with DNA or genes, but I'm open to suggestions) Combined somehow with food - preferably vegetables/ fruit/ meat/eggs etc. Definitely not grains or dairy - we take autistic kids off those 2 food groups straight away.
Green in it somewhere? I somehow associates healthy living / whole foods nutrition with the colour green. You guys know more about colours than me :-)
Maybe a helix could morph into a body shape filled with foods (along the lines of "you are what you eat" or something...)

Target Market(s)

The majority of my clients to date are people in their 40's wanting to improve their health or their children's health.

Industry/Entity Type

Nutrition

Contact Information for Business Card

Front of card:
Dr Moira Pellton (B App Sci, PhD Molecular Pathology)
Certified Vitacorde Practitioner and RUNE Nutritionist
52 Tallowby Rd, Tallowby
0417386254
dr.moirapellton@quillmail.com
drmoirapellton.com.au
Back of card:
Small Photo of me, Dr Moira Pellton
Specialises in Autism, ADHD, Fussy Eaters, Gut Issues, Food Intolerances, Healthy Ageing

Logo Text

Dr Moira Pellton

Logo styles of interest
Pictorial/Combination Logo
Character Logo
Requirements
Must have
• A logo showing a clear link between genes and nutrition
The box for what I want written on the card is not coming up when I try to edit so I'll put it here....
Front of card:
Dr Moira Pellton
(B App Sci, PhD Molecular Pathology) in smaller writing under my name

Certified Nutrigenomist
Certified RUNE Nutritionist

then use your nice symbols for the address, ph etc as below

52 Tallowby Rd, Tallowby
0417386254
dr.moirapellton@quillmail.com
www.drmoirapellton.com.au

Back of card:
Small Photo of me
Dr Moira Pellton
Specialises in:
Nutrigenomics
Healthy Ageing
Autism / ADHD
Gut Issues
Food Intolerances
Should not have
• No bread or grains of any sort
No dairy - milk cheese etc

```html
<!DOCTYPE html>
<html lang="en">
<head>
<meta charset="utf-8">
<title>Dr Moira Pellton – Business Card</title>
<link href="https://fonts.googleapis.com/css2?family=Tenor+Sans&display=swap" rel="stylesheet">
<style>
  :root {
    --stage: #000000;
    --card-front: #ffffff;
    --card-back: #cdd1ca;
    --brand-green: #1e6b3a;
    --ink: #2a2a2a;
    --rule: #6f736d;
    --photo-tone-a: #6b4a3c;
    --photo-tone-b: #c9a07f;
  }
  * { box-sizing: border-box; margin: 0; padding: 0; }
  html, body {
    width: 1200px; height: 849px; overflow: hidden;
    background: var(--stage);
    font-family: "Tenor Sans", sans-serif;
    color: var(--ink);
  }
  .stage { position: relative; width: 1200px; height: 849px; }
  .card {
    position: absolute; top: 322px; width: 358px; height: 204px;
    border-radius: 11px; overflow: hidden;
  }
  .card--front { left: 228px; background: var(--card-front); }
  .card--back { left: 613px; background: var(--card-back); }

  .brand-mark {
    position: absolute; left: 20px; top: 66px; width: 82px;
    display: flex; flex-direction: column; align-items: center; gap: 6px;
  }
  .brand-mark__dot { width: 14px; height: 14px; border-radius: 50%; background: var(--brand-green); }
  .brand-mark__name { font-size: 13px; color: var(--brand-green); letter-spacing: 0.3px; }

  .divider { position: absolute; left: 128px; top: 17px; width: 1px; height: 168px; background: var(--rule); }

  .front-info { position: absolute; left: 143px; top: 13px; }
  .name { font-size: 19px; color: var(--brand-green); line-height: 1.2; font-weight: 400; }
  .quals { font-size: 8.5px; margin-top: 7px; }
  .certs { font-size: 10px; line-height: 12px; margin-top: 22px; }
  .contacts { list-style: none; margin-top: 23px; font-size: 10px; }
  .contacts li { display: flex; align-items: center; gap: 10px; height: 11.5px; }
  .contacts li:last-child { margin-top: 3px; }
  .contacts svg { width: 9px; height: 9px; fill: var(--ink); flex: none; }

  .portrait {
    position: absolute; left: 149px; top: 17px; width: 61px; height: 81px;
    border-radius: 4px;
    background: linear-gradient(160deg, var(--photo-tone-a), var(--photo-tone-b));
  }
  .back-name {
    position: absolute; left: 0; right: 0; top: 104px;
    text-align: center; font-size: 16px; color: var(--brand-green); font-weight: 400;
  }
  .back-rule { position: absolute; left: 0; right: 0; top: 147px; height: 1px; background: var(--rule); }
  .specialties { position: absolute; left: 19px; top: 158px; font-size: 8px; }
  .specialties__list { list-style: none; display: flex; gap: 6px; margin-top: 5px; }
</style>
</head>
<body>
<main class="stage">
  <section class="card card--front" aria-label="Card front">
    <div class="brand-mark">
      <span class="brand-mark__dot"></span>
      <span class="brand-mark__name">Pellton</span>
    </div>
    <div class="divider"></div>
    <div class="front-info">
      <h1 class="name">Dr Moira Pellton</h1>
      <p class="quals">(B App Sci, PhD Molecular Pathology)</p>
      <p class="certs">Certified Nutrigenomist<br>Certified RUNE Nutritionist</p>
      <ul class="contacts">
        <li><svg viewBox="0 0 10 10"><path d="M0 2h10v6H0z"/></svg>52 Tallowby Rd, Tallowby</li>
        <li><svg viewBox="0 0 10 10"><path d="M2 0l2 2-1 1.5c.8 1.6 2 2.8 3.5 3.5L8 6l2 2-1.5 2C4 9.5.5 6 0 1.5z"/></svg>0417386254</li>
        <li><svg viewBox="0 0 10 10"><path d="M0 2h10v6H0zM1 3l4 3 4-3z" fill-rule="evenodd"/></svg>dr.moirapellton@quillmail.com</li>
        <li><svg viewBox="0 0 10 10"><path d="M5 0a5 5 0 110 10A5 5 0 015 0zm0 1.5a3.5 3.5 0 100 7 3.5 3.5 0 000-7z" fill-rule="evenodd"/></svg>www.drmoirapellton.com.au</li>
      </ul>
    </div>
  </section>

  <section class="card card--back" aria-label="Card back">
    <div class="portrait" role="img" aria-label="Small portrait photo of Dr Moira Pellton"></div>
    <h2 class="back-name">Dr Moira Pellton</h2>
    <div class="back-rule"></div>
    <div class="specialties">
      <p>Specialises in:</p>
      <ul class="specialties__list">
        <li>• Nutrigenomics</li>
        <li>• Healthy Ageing</li>
        <li>• Autism / ADHD</li>
        <li>• Gut Issues</li>
        <li>• Food Intolerances</li>
      </ul>
    </div>
  </section>
</main>
</body>
</html>
```